401K Retirement Plan Consultant

Professional & clean lines - not overly busy. We offer two services - 401k administration and HSA administration. Based on the outskirts of Charlotte NC. Communicate the services we offer along with the financial institutions that we work with. Mixture of icons and people pictures.

Current website - tvh401k.com,
It is presently very amateurish.

```html
<!DOCTYPE html>
<html lang="en">
<head>
<meta charset="utf-8">
<title>TVH401k Employee Benefits</title>
<link href="https://fonts.googleapis.com/css2?family=Bebas+Neue&family=Outfit:wght@300;400;500;600&family=Poppins:wght@500;600&display=swap" rel="stylesheet">
<style>
:root{
  --blue:#0f14f2;
  --navy:#0b0b2e;
  --ink:#111111;
  --muted:#3a3a3a;
  --white:#ffffff;
  --black:#000000;
  --dark:#0c0c0c;
  --line:#2a2a2a;
}
*{margin:0;padding:0;box-sizing:border-box}
html,body{width:1200px;height:2838px;overflow:hidden}
body{position:relative;background:var(--white);font-family:"Outfit",sans-serif;color:var(--ink)}
.abs{position:absolute}
/* header */
.brand{left:141px;top:14px;font-family:"Poppins",sans-serif;font-weight:600;font-size:30px;color:var(--navy);letter-spacing:.5px}
.nav a{position:absolute;top:24px;font-size:13px;color:var(--ink);text-decoration:none}
.btn-contact{left:957px;top:13px;width:101px;height:35px;background:var(--blue);color:var(--white);border-radius:3px;font-size:13px;display:flex;align-items:center;justify-content:center}
/* hero */
.hero{left:0;top:63px;width:1200px;height:529px;background:linear-gradient(100deg,#2e2a14 0%,#6b5a2a 30%,#b98d3f 55%,#d6a452 70%,#8a6a2c 100%)}
.hero-title{left:141px;top:214px;font-family:"Bebas Neue",sans-serif;font-size:60px;line-height:57px;color:var(--white);width:440px}
/* services */
.section-title{font-family:"Poppins",sans-serif;font-weight:600;font-size:33px;color:var(--ink)}
.tile{position:absolute;width:180px;height:180px;display:flex;flex-direction:column;align-items:center;justify-content:center;text-align:center}
.tile::before{content:"";position:absolute;left:28px;top:28px;width:124px;height:124px;background:var(--white);border-radius:26px;transform:rotate(45deg);box-shadow:0 6px 22px rgba(0,0,0,.09)}
.tile svg,.tile span{position:relative}
.tile span{font-family:"Outfit",sans-serif;font-weight:500;font-size:13.5px;line-height:17px;color:var(--ink);margin-top:6px}
/* welcome */
.welcome{left:0;top:1093px;width:1200px;height:612px;background:linear-gradient(125deg,#141414 0%,#050505 40%,#1c1c1c 55%,#060606 70%,#181818 100%)}
.welcome-photo{left:141px;top:1178px;width:441px;height:441px;border-radius:6px;background:linear-gradient(170deg,#7d6c9a 0%,#c08aa0 45%,#e6a070 75%,#d87a3e 100%)}
.welcome-title{left:617px;top:1190px;font-family:"Poppins",sans-serif;font-weight:600;font-size:33px;color:var(--white)}
.welcome-copy{left:617px;top:1240px;width:441px;font-size:13px;line-height:21.6px;color:#e6e6e6;font-weight:300}
.welcome-copy p{margin-bottom:8px}
.welcome-copy p.bullet{margin-bottom:5px}
.welcome-copy strong{font-weight:600;color:var(--white)}
/* other services */
.other-item{position:absolute;left:141px;display:flex;align-items:center;gap:18px;font-family:"Outfit",sans-serif;font-weight:600;font-size:17px;color:var(--ink)}
.other-photo{left:617px;top:1790px;width:441px;height:441px;border-radius:6px;background:linear-gradient(180deg,#a8b6c4 0%,#5f7f8e 30%,#5c7a3c 60%,#3d5226 80%,#a32125 100%)}
/* partners */
.footer{left:0;top:2422px;width:1200px;height:384px;background:var(--black)}
.partners{left:141px;top:2315px;width:917px;height:169px;background:var(--white);border-radius:8px;box-shadow:0 4px 18px rgba(0,0,0,.08)}
.partners h3{position:absolute;top:36px;width:100%;text-align:center;font-family:"Poppins",sans-serif;font-weight:600;font-size:23px;color:var(--ink)}
.partner{position:absolute;top:96px;font-family:"Outfit",sans-serif;font-weight:500;font-size:21px;color:#1d2a6b;display:flex;align-items:center;gap:6px}
.partner i{display:inline-block;width:12px;height:12px;background:#1d2a6b;border-radius:50%}
/* footer */
.footer-brand{left:141px;top:2535px;font-family:"Poppins",sans-serif;font-weight:600;font-size:42px;color:var(--white)}
.footer-nav a{position:absolute;top:2564px;font-size:13px;color:var(--white);text-decoration:none}
.footer-rule{left:141px;top:2653px;width:917px;height:1px;background:var(--line)}
.contact-dot{position:absolute;top:2701px;width:42px;height:42px;border-radius:50%;background:#2b2b2b;display:flex;align-items:center;justify-content:center}
.contact-text{position:absolute;top:2703px;font-size:12.5px;line-height:17px;color:var(--white);font-weight:300}
.contact-text b{display:block;font-weight:500;margin-bottom:2px}
.sep{position:absolute;top:2710px;width:1px;height:27px;background:#6a6a6a}
.bottom-bar{left:0;top:2806px;width:1200px;height:32px;background:var(--blue);color:var(--white);font-size:12px;display:flex;align-items:center;justify-content:center;font-weight:300}
</style>
</head>
<body>

<header>
  <div class="abs brand">TVH401k</div>
  <nav class="nav">
    <a style="left:785px">Home</a>
    <a style="left:862px">About Us</a>
    <a class="btn-contact abs" style="top:13px">Contact Us</a>
  </nav>
</header>

<section>
  <div class="abs hero" role="img" aria-label="Family of five walking through a sunlit meadow by a lake with a forest behind"></div>
  <h1 class="abs hero-title">TVH401K has been providing employee benefits services since 1987</h1>
</section>

<section class="services">
  <h2 class="abs section-title" style="left:0;width:1200px;text-align:center;top:670px">Our Services</h2>

  <div class="tile" style="left:135px;top:722px">
    <svg width="50" height="50" viewBox="0 0 50 50" fill="none" stroke="#0f14f2" stroke-width="2"><path d="M18 8h14l-4 8h-6z"/><path d="M22 16c-10 6-12 26 3 26s13-20 3-26"/><path d="M28 26c-2-2-6-1-6 1s6 2 6 4-4 3-6 1M25 22v3M25 33v3"/><rect x="6" y="34" width="10" height="10"/><rect x="36" y="34" width="10" height="10"/></svg>
    <span>Open Architecture<br>Platform</span>
  </div>
  <div class="tile" style="left:322px;top:722px">
    <svg width="50" height="50" viewBox="0 0 50 50" fill="none" stroke="#0f14f2" stroke-width="2"><rect x="12" y="6" width="30" height="38" rx="2"/><circle cx="13" cy="16" r="8"/><path d="M15 13c-1-1-4-1-4 1s4 1 4 3-3 2-4 1M13 10v2M13 20v2M24 16h14M20 24h18M20 30h18M20 36h18"/></svg>
    <span>IRS 5500 &amp;<br>1099-R's</span>
  </div>
  <div class="tile" style="left:510px;top:722px">
    <svg width="50" height="50" viewBox="0 0 50 50" fill="none" stroke="#0f14f2" stroke-width="2"><circle cx="22" cy="14" r="7"/><path d="M8 44c0-12 6-18 14-18s14 6 14 18"/><rect x="28" y="32" width="18" height="12"/><path d="M34 32v-3h6v3M28 37h18"/></svg>
    <span>Employer Allocation<br>Preparation</span>
  </div>
  <div class="tile" style="left:696px;top:722px">
    <svg width="50" height="50" viewBox="0 0 50 50" fill="none" stroke="#0f14f2" stroke-width="2"><rect x="14" y="4" width="32" height="20"/><path d="M18 10h10M18 16h22M32 10h10"/><circle cx="10" cy="30" r="3"/><circle cx="24" cy="32" r="3"/><circle cx="38" cy="32" r="3"/><path d="M4 44c0-6 3-9 6-9s6 3 6 9M18 46c0-6 3-9 6-9s6 3 6 9M32 46c0-6 3-9 6-9s6 3 6 9"/></svg>
    <span>Employee<br>Education</span>
  </div>
  <div class="tile" style="left:883px;top:722px">
    <svg width="50" height="50" viewBox="0 0 50 50" fill="none" stroke="#0f14f2" stroke-width="2"><path d="M12 4h20l8 8v34H12z"/><path d="M32 4v8h8M17 18h18M17 24h18M17 30h18M17 36h18"/></svg>
    <span>Plan Design &amp;<br>Document Services</span>
  </div>

  <div class="tile" style="left:228px;top:838px">
    <svg width="50" height="50" viewBox="0 0 50 50" fill="none" stroke="#0f14f2" stroke-width="2"><rect x="10" y="6" width="26" height="34" rx="2"/><path d="M18 6v-2h10v2"/><circle cx="30" cy="30" r="7"/><path d="M35 35l8 8M16 16h14M16 22h8"/><rect x="4" y="34" width="10" height="12"/></svg>
    <span>Non-Discrimination<br>Testing</span>
  </div>
  <div class="tile" style="left:415px;top:840px">
    <svg width="50" height="50" viewBox="0 0 50 50" fill="none" stroke="#0f14f2" stroke-width="2"><rect x="24" y="4" width="22" height="16"/><path d="M28 9h14M28 14h10"/><circle cx="14" cy="14" r="6"/><path d="M4 34c0-8 4-12 10-12s10 4 10 12"/><rect x="18" y="28" width="24" height="14"/><path d="M4 44h44"/></svg>
    <span>HSA<br>Administration</span>
  </div>
  <div class="tile" style="left:602px;top:836px">
    <svg width="50" height="50" viewBox="0 0 50 50" fill="none" stroke="#0f14f2" stroke-width="2"><rect x="8" y="6" width="34" height="32" rx="2"/><circle cx="25" cy="22" r="8"/><path d="M27 19c-1-1-4-1-4 1s4 1 4 3-3 2-4 1M25 16v2M25 26v2M4 40h42l-4 4H8z"/></svg>
    <span>FSA, HRA and<br>Dependent Care</span>
  </div>
  <div class="tile" style="left:789px;top:840px">
    <svg width="50" height="50" viewBox="0 0 50 50" fill="none" stroke="#0f14f2" stroke-width="2"><path d="M8 4h24l6 6v32H8z"/><path d="M13 12h18M13 18h18M13 24h10"/><circle cx="18" cy="34" r="5"/><path d="M30 26l14 14-4 4-14-14z"/></svg>
    <span>COBRA<br>Administration</span>
  </div>
</section>

<section>
  <div class="abs welcome"></div>
  <div class="abs welcome-photo" role="img" aria-label="Young girl with outstretched arms riding on a parent's shoulders at sunset"></div>
  <h2 class="abs welcome-title">Welcome to TVH401k</h2>
  <div class="abs welcome-copy">
    <p>401k TVH has been providing employee benefit services since 1987. &nbsp; Our plans gives you the flexibility to customize a retirement plan that meets the specific needs of your company and the employees. Our IRS approved 401(k) plans are:</p>
    <p class="bullet">• Designed especially for smaller plans</p>
    <p class="bullet">• Simple to operate and maintain</p>
    <p>• Low-cost recordkeeping and investments</p>
    <p>Most people realize that, we all have to accept more responsibility for saving for our own retirement. &nbsp;It's widely accepted that Social Security is only meant to provide a modest percentage of your retirement income—so Social Security alone will not be enough.</p>
    <p>Setting up an employee retirement plan can be a smart way to provide for one of your key assets <strong>– your people.</strong></p>
    <p>Contact us today to request a custom fee comparison or a quote for a startup plan. &nbsp;It's quick and easy.</p>
  </div>
</section>

<section>
  <h2 class="abs section-title" style="left:141px;top:1826px">Other Services</h2>
  <div class="other-item" style="top:1880px">
    <svg width="40" height="40" viewBox="0 0 40 40" fill="none" stroke="#0f14f2" stroke-width="2"><path d="M20 22c-8-5-10-9-10-12a5 5 0 0 1 10-1 5 5 0 0 1 10 1c0 3-2 7-10 12z"/><path d="M18 10h4M20 8v4M2 20l6 16h4M38 20l-6 16h-4"/></svg>
    <span>HSA - Health Saving Account</span>
  </div>
  <div class="other-item" style="top:1945px">
    <svg width="40" height="40" viewBox="0 0 40 40" fill="none" stroke="#0f14f2" stroke-width="2"><rect x="6" y="6" width="28" height="14" rx="2"/><circle cx="20" cy="13" r="3"/><path d="M2 28h10l6 4h12l6-6M2 36h8"/></svg>
    <span>FSA - Flexible Spending Account</span>
  </div>
  <div class="other-item" style="top:2011px">
    <svg width="40" height="40" viewBox="0 0 40 40" fill="none" stroke="#0f14f2" stroke-width="2"><circle cx="20" cy="20" r="12"/><path d="M6 12a16 16 0 0 1 28-2M34 28a16 16 0 0 1-28 2"/><path d="M23 16c-1-2-6-2-6 1s6 2 6 5-5 3-6 1M20 12v3M20 26v3"/></svg>
    <span>HRA - Health Reimbursement Account</span>
  </div>
  <div class="other-item" style="top:2076px">
    <svg width="40" height="40" viewBox="0 0 40 40" fill="none" stroke="#0f14f2" stroke-width="2"><path d="M6 2h20l6 6v10M6 2v36h14"/><path d="M12 14h8M16 10v8M10 26h8"/><path d="M30 22l8 3v6c0 4-4 7-8 8-4-1-8-4-8-8v-6z"/></svg>
    <span>COBRA - Health Insurance Continuation</span>
  </div>
  <div class="other-item" style="top:2144px">
    <svg width="40" height="40" viewBox="0 0 40 40" fill="none" stroke="#0f14f2" stroke-width="2"><circle cx="10" cy="8" r="4"/><circle cx="28" cy="6" r="4"/><path d="M4 38V20c0-4 3-6 6-6s6 2 6 6v18M22 38V18c0-4 3-6 6-6s6 2 6 6v20"/><circle cx="19" cy="24" r="3"/></svg>
    <span>DEPENDENT CARE - Dependent Care</span>
  </div>
  <div class="abs other-photo" role="img" aria-label="Older couple in red jackets seated on a bench overlooking green alpine mountains"></div>
</section>

<footer>
  <div class="abs footer"></div>
  <div class="abs partners">
    <h3>Our Partners</h3>
    <div class="partner" style="left:34px"><i></i>Northgate</div>
    <div class="partner" style="left:182px">Benefyn</div>
    <div class="partner" style="left:327px">Keystone</div>
    <div class="partner" style="left:465px">Harbor Funds</div>
    <div class="partner" style="left:620px">Vantix</div>
    <div class="partner" style="left:736px">Meridian Ledger</div>
  </div>

  <div class="abs footer-brand">TVH401k</div>
  <nav class="footer-nav">
    <a style="left:666px">Home</a>
    <a style="left:820px">About Us</a>
    <a style="left:993px">Contact Us</a>
  </nav>
  <div class="abs footer-rule"></div>

  <div class="contact-dot" style="left:140px"><svg width="18" height="14" viewBox="0 0 18 14" fill="none" stroke="#fff" stroke-width="1.5"><rect x="1" y="1" width="16" height="12"/><path d="M1 1l8 7 8-7"/></svg></div>
  <div class="contact-text" style="left:198px"><b>EMAIL</b>Service@tvh401k.com</div>
  <div class="sep" style="left:360px"></div>

  <div class="contact-dot" style="left:397px"><svg width="14" height="18" viewBox="0 0 14 18" fill="#fff"><path d="M7 0a7 7 0 0 0-7 7c0 5 7 11 7 11s7-6 7-11a7 7 0 0 0-7-7zm0 9.5a2.5 2.5 0 1 1 0-5 2.5 2.5 0 0 1 0 5z"/></svg></div>
  <div class="contact-text" style="left:457px"><b>TVH 401k</b>1820 Lakeshore Pkwy Suite<br>305 Riverbend SC 29700</div>
  <div class="sep" style="left:658px"></div>

  <div class="contact-dot" style="left:694px"><svg width="18" height="18" viewBox="0 0 18 18" fill="#fff"><path d="M4 1l3 4-2 2c1 3 3 5 6 6l2-2 4 3-2 3C8 17 1 10 1 3z"/></svg></div>
  <div class="contact-text" style="left:755px"><b>PHONE</b>1 704 555 0142</div>
  <div class="sep" style="left:879px"></div>

  <div class="contact-dot" style="left:916px"><svg width="18" height="16" viewBox="0 0 18 16" fill="#fff"><rect x="4" y="0" width="10" height="4"/><rect x="0" y="5" width="18" height="7" rx="1"/><rect x="4" y="10" width="10" height="6" stroke="#2b2b2b"/></svg></div>
  <div class="contact-text" style="left:977px"><b>FAX</b>1 877 555 0187</div>

  <div class="abs bottom-bar">© 2024 Tvh401k. All Rights Reserved | Privacy Policy</div>
</footer>

</body>
</html>
```